Hexagon Honey Bottle Design, simple and elegant.

Bottle description:
BODY HEIGHT With cap 8.75cm
Without cap 8.6cm
DIAMETER Inner 4.4cm
Outer 5.2cm
Label height only has to be = 6cm height x (3.4X6) length of one hexagonal box is 3.4cm
See through bottle with black cap.
Concept of design:
Elegant, Simple, no pictures of bees, pictures of honeycomb, wooden honey stick, or drooling honey from either is ok. Simple colors. (Designer's discretion)
Wordings:
Hex1
Product of Yemen
Header:
MAROL /TUVI/ (Brand name)
Explanatory below header
Yemen Sidr Honey from The Valley Qarbeen (100% Pure)
(name of honey)
250g
Optional
Hex2
Pure
=
No Additives (not even natural additives)
Hex3
Raw
=
Unheated, Unpasteurized, Unprocessed honey
Hex4
Natural
=
No added color, artificial flavor, or synthetic substance
Hex5
RENOWNED
=
Very well known by honey lovers
(Natural Pure Raw and Renowned) wordings to be on a suitable place on the bottle (maybe on the cap) -
Hex6
Imported By
The Copperfield Trading Pte Ltd
No. 317, Larkspur Grove Road, #09-12
Larkspur Grove Plaza
Singapore 174593
Wordings can be rearranged - its up to the designer's discretion where and how to place them and in which order.-
Designer must be willing to do numerous changes as the design develops

```html
<!DOCTYPE html>
<html lang="en">
<head>
<meta charset="utf-8">
<title>Marol Tuvi – Yemen Sidr Honey Label</title>
<link rel="stylesheet" href="https://fonts.googleapis.com/css2?family=Oranienbaum&family=Roboto+Condensed:wght@400;500&display=swap">
<style>
  :root{
    --ink:#0c0c0c;
    --gold:#f2d27a;
    --gold-deep:#c9a23a;
    --cap-gold:#f3dc93;
    --cap-gold-light:#f8e8b4;
    --clear:#c6c6c6;
    --clear-light:#d2d0c6;
    --paper:#ffffff;
    --dim:#1a1a1a;
    --note:#7a7a7a;
    --amber-1:#f0b23a;
    --amber-2:#a8651a;
  }
  html,body{margin:0;padding:0;overflow:hidden;background:var(--paper);}
  .artboard{width:1200px;height:1018px;position:relative;overflow:hidden;background:var(--paper);}
  .artboard svg{display:block;}
  .serif{font-family:"Oranienbaum",serif;}
  .sans{font-family:"Roboto Condensed",sans-serif;}
  .dim-label{font-family:"Roboto Condensed",sans-serif;font-size:19px;fill:var(--dim);}
  .material-note{font-family:"Roboto Condensed",sans-serif;font-size:17px;font-weight:500;fill:var(--note);letter-spacing:.5px;}
  .brand-name{font-family:"Oranienbaum",serif;fill:var(--ink);}
  .ribbon-text{font-family:"Oranienbaum",serif;font-size:17px;fill:var(--ink);}
  .seal-ribbon-text{font-family:"Oranienbaum",serif;font-size:14px;fill:var(--paper);}
  .origin-text{font-family:"Oranienbaum",serif;font-size:18px;fill:var(--paper);}
  .importer{font-family:"Roboto Condensed",sans-serif;font-size:12.5px;fill:var(--paper);}
  .claim{font-family:"Roboto Condensed",sans-serif;font-size:11px;fill:var(--paper);}
  .cap-claim{font-family:"Oranienbaum",serif;font-size:12px;fill:var(--ink);letter-spacing:.6px;}
</style>
</head>
<body>
<div class="artboard">
<svg width="1200" height="1018" viewBox="0 0 1200 1018" xmlns="http://www.w3.org/2000/svg">
  <defs>
    <linearGradient id="dipper-tone" x1="0" y1="0" x2="1" y2="1">
      <stop offset="0" stop-color="var(--amber-1)"/>
      <stop offset="1" stop-color="var(--amber-2)"/>
    </linearGradient>
    <linearGradient id="comb-window" x1="0" y1="0" x2="0" y2="1">
      <stop offset="0" stop-color="var(--clear)"/>
      <stop offset="1" stop-color="var(--clear-light)"/>
    </linearGradient>
    <radialGradient id="comb-seal" cx="0.5" cy="0.4" r="0.6">
      <stop offset="0" stop-color="var(--cap-gold-light)"/>
      <stop offset="1" stop-color="var(--cap-gold)"/>
    </radialGradient>
    <clipPath id="label-clip"><rect x="138" y="586" width="656" height="385" rx="18"/></clipPath>
    <path id="cap-arc" d="M 942 570 A 94 94 0 0 0 1130 570"/>
  </defs>

  <!-- ===== Wrap label dimensions ===== -->
  <g class="wrap-dimensions" stroke="var(--dim)" stroke-width="1" fill="none">
    <line x1="138" y1="547" x2="794" y2="547"/>
    <line x1="138" y1="533" x2="138" y2="565"/>
    <line x1="356" y1="535" x2="356" y2="560"/>
    <line x1="574" y1="535" x2="574" y2="560"/>
    <line x1="794" y1="533" x2="794" y2="565"/>
    <line x1="97" y1="586" x2="97" y2="971"/>
    <line x1="84" y1="586" x2="120" y2="586"/>
    <line x1="84" y1="971" x2="120" y2="971"/>
    <line x1="130" y1="572" x2="168" y2="600"/>
  </g>
  <text class="dim-label" x="247" y="539" text-anchor="middle">3.4 cm</text>
  <text class="dim-label" x="465" y="539" text-anchor="middle">3.4 cm</text>
  <text class="dim-label" x="684" y="539" text-anchor="middle">3.4 cm</text>
  <text class="dim-label" transform="translate(88 778) rotate(-90)" text-anchor="middle">6 cm</text>
  <text class="material-note" x="128" y="551" text-anchor="end">TRANSPARENT</text>
  <text class="material-note" x="128" y="571" text-anchor="end">MATERIAL</text>

  <!-- ===== Wrap label ===== -->
  <g class="wrap-label" clip-path="url(#label-clip)">
    <rect class="comb-window" x="138" y="586" width="656" height="184" fill="url(#comb-window)" role="img" aria-label="Gold honeycomb pattern printed on transparent film"/>
    <rect x="138" y="770" width="656" height="5" fill="var(--ink)"/>
    <rect class="gold-band" x="138" y="775" width="656" height="35" fill="var(--gold)"/>
    <rect class="black-base" x="138" y="810" width="656" height="161" fill="var(--ink)"/>
    <!-- dipper illustration area -->
    <rect class="dipper-art" x="372" y="586" width="132" height="130" rx="10" fill="url(#dipper-tone)" opacity=".85" role="img" aria-label="Wooden honey dipper dripping honey into the hexagon"/>
  </g>
  <g class="panel-folds" stroke="var(--ink)" stroke-width="1" stroke-dasharray="5 5">
    <line x1="356" y1="586" x2="356" y2="971"/>
    <line x1="574" y1="586" x2="574" y2="971"/>
  </g>

  <!-- 100% pure badge -->
  <g class="pure-badge">
    <polygon points="528,612 551,625 551,650 528,663 505,650 505,625" fill="var(--ink)" stroke="var(--paper)" stroke-width="2.5"/>
    <text class="sans" x="528" y="635" text-anchor="middle" font-size="12" font-weight="500" fill="var(--paper)">100%</text>
    <text class="sans" x="528" y="649" text-anchor="middle" font-size="12" font-weight="500" fill="var(--paper)">PURE</text>
  </g>

  <!-- central hexagon -->
  <g class="brand-hex">
    <polygon points="466,656 571,714 571,822 466,880 361,822 361,714" fill="var(--gold-deep)"/>
    <polygon points="466,662 565,717 565,819 466,874 367,819 367,717" fill="var(--ink)"/>
    <polygon points="466,670 558,721 558,815 466,866 374,815 374,721" fill="var(--paper)"/>
    <text class="brand-name" x="466" y="782" text-anchor="middle" font-size="56">Marol</text>
    <text class="brand-name" x="518" y="807" text-anchor="middle" font-size="24">Tuvi</text>
  </g>

  <!-- name ribbon -->
  <g class="name-ribbon">
    <polygon points="370,874 564,874 556,896 564,918 370,918 378,896" fill="var(--gold)" stroke="var(--ink)" stroke-width="1.5"/>
    <text class="ribbon-text" x="467" y="893" text-anchor="middle">Yemen Sidr Honey from</text>
    <text class="ribbon-text" x="467" y="912" text-anchor="middle">The Valley Qarbeen</text>
  </g>
  <text class="origin-text" x="439" y="947" text-anchor="middle">Product of Yemen</text>
  <line x1="512" y1="929" x2="512" y2="951" stroke="var(--paper)" stroke-width="1.2"/>
  <text class="origin-text" x="539" y="947" text-anchor="middle">250g</text>

  <!-- importer panel -->
  <g class="importer-panel">
    <text class="importer" x="240" y="851" text-anchor="middle">Imported By</text>
    <text class="importer" x="240" y="867" text-anchor="middle">The Copperfield Trading Pte Ltd</text>
    <text class="importer" x="240" y="883" text-anchor="middle">No. 317, Larkspur Grove</text>
    <text class="importer" x="240" y="899" text-anchor="middle">Road, #09-12</text>
    <text class="importer" x="240" y="915" text-anchor="middle">Larkspur Grove Plaza</text>
    <text class="importer" x="240" y="931" text-anchor="middle">Singapore 174593</text>
  </g>

  <!-- claims panel -->
  <g class="claims-icons" fill="none" stroke="var(--gold)" stroke-width="1.3">
    <circle cx="608" cy="833" r="12"/><path d="M602 839 C602 829 610 825 615 826 C615 833 610 839 602 839 M602 839 L610 831"/>
    <circle cx="608" cy="865" r="12"/><path d="M603 871 L611 860 M609 858 l4 4"/>
    <circle cx="608" cy="897" r="12"/><path d="M600 889 L616 905 M604 902 l8 -10"/>
    <circle cx="608" cy="941" r="12"/><path d="M604 947 v-9 l3 -5 l2 5 h4 v9 z"/>
  </g>
  <g class="claims-text">
    <text class="claim" x="627" y="830">PURE: No Additives</text>
    <text class="claim" x="627" y="843">(not even natural additives)</text>
    <text class="claim" x="627" y="862">RAW: Unheated, Unpasteurized,</text>
    <text class="claim" x="627" y="875">Unprocessed honey</text>
    <text class="claim" x="627" y="894">NATURAL: No added color,</text>
    <text class="claim" x="627" y="907">artificial flavor, or</text>
    <text class="claim" x="627" y="919">synthetic substance</text>
    <text class="claim" x="627" y="938">RENOWNED: Very well</text>
    <text class="claim" x="627" y="951">known by honey lovers</text>
  </g>

  <!-- ===== Cap seal dimensions ===== -->
  <g class="cap-dimensions" stroke="var(--dim)" stroke-width="1" fill="none">
    <line x1="924" y1="438" x2="1148" y2="438"/>
    <line x1="924" y1="426" x2="924" y2="461"/>
    <line x1="1148" y1="426" x2="1148" y2="461"/>
    <line x1="892" y1="458" x2="892" y2="1004"/>
    <line x1="878" y1="458" x2="906" y2="458"/>
    <line x1="878" y1="1004" x2="906" y2="1004"/>
    <line x1="878" y1="684" x2="1000" y2="684" stroke-dasharray="6 5"/>
  </g>
  <text class="dim-label" x="1034" y="432" text-anchor="middle">3.5 cm</text>
  <text class="dim-label" transform="translate(885 572) rotate(-90)" text-anchor="middle">3.5 cm</text>
  <text class="dim-label" transform="translate(885 844) rotate(-90)" text-anchor="middle">5 cm</text>

  <!-- ===== Cap seal ===== -->
  <g class="cap-strip">
    <rect x="1000" y="672" width="64" height="332" fill="var(--ink)"/>
    <line x1="1006" y1="672" x2="1006" y2="1004" stroke="var(--gold)" stroke-width="1.5"/>
    <line x1="1058" y1="672" x2="1058" y2="1004" stroke="var(--gold)" stroke-width="1.5"/>
  </g>
  <g class="cap-seal">
    <circle cx="1036" cy="570" r="112" fill="var(--paper)" stroke="#d8d8d8" stroke-width="1"/>
    <circle cx="1036" cy="570" r="110" fill="url(#comb-seal)" role="img" aria-label="Soft honeycomb pattern"/>
    <text class="brand-name" x="1036" y="542" text-anchor="middle" font-size="46">Marol</text>
    <text class="brand-name" x="1076" y="561" text-anchor="middle" font-size="19">Tuvi</text>
    <rect x="964" y="576" width="144" height="36" fill="var(--ink)" stroke="var(--paper)" stroke-width="1.2"/>
    <text class="seal-ribbon-text" x="1036" y="591" text-anchor="middle">Yemen Sidr Honey from</text>
    <text class="seal-ribbon-text" x="1036" y="606" text-anchor="middle">The Valley Qarbeen</text>
    <text class="serif" x="1036" y="630" text-anchor="middle" font-size="13" fill="var(--ink)">– 250g –</text>
    <text class="cap-claim"><textPath href="#cap-arc" startOffset="14%" text-anchor="middle">PURE</textPath></text>
    <text class="cap-claim"><textPath href="#cap-arc" startOffset="40%" text-anchor="middle">NATURAL</textPath></text>
    <text class="cap-claim"><textPath href="#cap-arc" startOffset="65%" text-anchor="middle">RAW</textPath></text>
    <text class="cap-claim"><textPath href="#cap-arc" startOffset="90%" text-anchor="middle">RENOWNED</textPath></text>
    <g class="seal-icons" fill="none" stroke="var(--ink)" stroke-width="1.2">
      <circle cx="944" cy="574" r="8"/>
      <circle cx="970" cy="632" r="8"/>
      <circle cx="1052" cy="660" r="8"/>
      <circle cx="1100" cy="634" r="8"/>
    </g>
  </g>
</svg>
</div>
</body>
</html>
```